Window Tinting

We are a window tinting company for automotive. Our main clientele has been the dealerships but now we are looking to expand to the general public. "Glidra" is actually short for gLidration (versus a measurement of time). We are hoping to make the "X" signature. Something easily noticed for later marketing. Right now since our name is kinda new, we'd rather the card scream "window tinting" versus our name being the main focus.. Window tint is a clean crisp aftermarket addition for vehicles and hopefully the business card can create that same attitude.

Industry/Entity Type

Automotive

Contact Information for Business Card

Glidra Shades Llc Ravi "Doc" Pellham
816 Lindcrest Ave. unit B
Brookmere, Vt 05491 802.571.2094

```html
<!DOCTYPE html>
<html lang="en">
<head>
<meta charset="utf-8">
<title>Glidra Shades – Business Card</title>
<link rel="stylesheet" href="https://fonts.googleapis.com/css2?family=Montserrat:wght@300&display=swap">
<style>
  :root {
    --card-blue: #0a82fd;
    --ink-dark: #222428;
    --paper-white: #ffffff;
    --text-grey: #3a3a3a;
  }
  html, body {
    margin: 0;
    padding: 0;
    width: 1200px;
    height: 702px;
    overflow: hidden;
  }
  .card {
    position: relative;
    width: 1200px;
    height: 702px;
    background: var(--card-blue);
    font-family: "Montserrat", Arial, sans-serif;
    font-weight: 300;
  }
  .brand-square {
    position: absolute;
    left: 472px;
    top: 151px;
    width: 255px;
    height: 318px;
    background: var(--ink-dark);
  }
  .brand-name {
    position: absolute;
    left: 742px;
    top: 255px;
    margin: 0;
    font-size: 106px;
    line-height: 1;
    font-weight: 300;
    color: var(--paper-white);
    white-space: nowrap;
  }
  .brand-rule {
    position: absolute;
    left: 737px;
    top: 368px;
    width: 324px;
    height: 20px;
    background: var(--ink-dark);
  }
  .contact-shadow {
    position: absolute;
    left: 85px;
    top: 481px;
    width: 1011px;
    height: 144px;
    background: var(--ink-dark);
  }
  .contact-panel {
    position: absolute;
    left: 103px;
    top: 494px;
    width: 993px;
    height: 146px;
    background: var(--paper-white);
    display: flex;
    flex-direction: column;
    justify-content: center;
    align-items: center;
  }
  .contact-line {
    margin: 0;
    font-size: 34px;
    line-height: 48px;
    color: var(--text-grey);
    letter-spacing: 2.6px;
    white-space: nowrap;
  }
</style>
</head>
<body>
  <main class="card">
    <div class="brand-square"></div>
    <h1 class="brand-name">Glidra</h1>
    <div class="brand-rule"></div>

    <div class="contact-shadow"></div>
    <section class="contact-panel">
      <p class="contact-line">Glidra Shades Llc Ravi “Doc” Pellham</p>
      <p class="contact-line">816 Lindcrest Ave. Unit B Brookmere, Vt 05491</p>
      <p class="contact-line">Phone:&nbsp; 802.571.2094</p>
    </section>
  </main>
</body>
</html>
```